Investment Business - Biz Card Design

Using the attached logo files, please create a superior business card design for Brantwell Holdings.

The "back" of the card should feature the logo (either in colour, or white/black over a feature colour)

The "front" of the card should feature: name, email, and phone

The design should be minimal and clean.

Target Market(s)

Business owners who need our investment services.

Industry/Entity Type

Business

```html
<!DOCTYPE html>
<html lang="en">
<head>
<meta charset="utf-8">
<title>Brantwell Holdings – Business Card</title>
<link rel="stylesheet" href="https://fonts.googleapis.com/css2?family=Arimo:wght@400;700&display=swap">
<style>
  :root {
    --backdrop: #e9e7e3;
    --navy: #0e2f86;
    --deep-blue: #13338f;
    --sky: #29a8df;
    --paper: #ffffff;
    --ink-grey: #6b6b6b;
    --card-shadow: 0 10px 26px rgba(0, 0, 0, 0.18);
  }
  * { box-sizing: border-box; margin: 0; padding: 0; }
  html, body {
    width: 1200px;
    height: 1000px;
    overflow: hidden;
    background: var(--backdrop);
    font-family: "Arimo", Arial, sans-serif;
  }
  .card {
    position: absolute;
    left: 280px;
    width: 640px;
    height: 366px;
    border-radius: 4px;
    box-shadow: var(--card-shadow);
  }
  .card-back {
    top: 70px;
    background: var(--navy);
    display: flex;
    align-items: center;
    justify-content: center;
  }
  .brand {
    display: flex;
    align-items: center;
    gap: 16px;
    font-weight: 700;
    white-space: nowrap;
  }
  .brand-mark {
    display: block;
    flex: none;
  }
  .card-back .brand { font-size: 44px; color: var(--paper); }
  .card-back .brand-mark { width: 30px; height: 30px; background: var(--sky); }

  .card-front {
    top: 484px;
    background: var(--paper);
  }
  .identity {
    position: absolute;
    left: 58px;
    top: 70px;
  }
  .person-name {
    font-size: 24px;
    color: var(--sky);
    font-weight: 400;
  }
  .person-role {
    margin-top: 6px;
    font-size: 22px;
    color: var(--deep-blue);
  }
  .divider {
    position: absolute;
    left: 300px;
    top: 40px;
    width: 2px;
    height: 280px;
    background: var(--sky);
  }
  .card-front .brand {
    position: absolute;
    left: 336px;
    top: 70px;
    font-size: 25px;
    color: var(--deep-blue);
    gap: 10px;
  }
  .card-front .brand-mark { width: 18px; height: 18px; background: var(--sky); }
  .contact-list {
    position: absolute;
    left: 336px;
    top: 232px;
    list-style: none;
  }
  .contact-item {
    display: flex;
    align-items: center;
    gap: 14px;
    font-size: 24px;
    color: var(--ink-grey);
    margin-bottom: 16px;
  }
  .contact-icon { width: 20px; height: 20px; flex: none; fill: var(--sky); }
</style>
</head>
<body>
  <section class="card card-back" aria-label="Card back">
    <div class="brand">
      <span class="brand-mark"></span>
      <span class="brand-name">Brantwell Holdings</span>
    </div>
  </section>

  <section class="card card-front" aria-label="Card front">
    <div class="identity">
      <h1 class="person-name">Daniel Hart</h1>
      <p class="person-role">CEO</p>
    </div>
    <div class="divider"></div>
    <div class="brand">
      <span class="brand-mark"></span>
      <span class="brand-name">Brantwell Holdings</span>
    </div>
    <ul class="contact-list">
      <li class="contact-item">
        <svg class="contact-icon" viewBox="0 0 24 24" aria-hidden="true">
          <path d="M6.6 10.8a15.1 15.1 0 0 0 6.6 6.6l2.2-2.2a1 1 0 0 1 1-.25 11.4 11.4 0 0 0 3.6.57 1 1 0 0 1 1 1V20a1 1 0 0 1-1 1A17 17 0 0 1 3 4a1 1 0 0 1 1-1h3.5a1 1 0 0 1 1 1c0 1.25.2 2.45.57 3.57a1 1 0 0 1-.25 1z"/>
        </svg>
        <span>0147 392 806</span>
      </li>
      <li class="contact-item">
        <svg class="contact-icon" viewBox="0 0 24 24" aria-hidden="true">
          <path d="M2 5h20v14H2z M3.5 6.5 12 13l8.5-6.5" fill="var(--sky)" stroke="#ffffff" stroke-width="1.4"/>
        </svg>
        <span>info@brantwellh.com</span>
      </li>
    </ul>
  </section>
</body>
</html>
```